Brightwell Letterhead

We would like a letterhead for our company. I have uploaded our logo.

Brightwell Peak Consulting
1450 W Corvin Rd Ste 310
Arlington, TX 76006
844-555-0172

```html
<!DOCTYPE html>
<html lang="en">
<head>
<meta charset="utf-8">
<title>Brightwell Peak Consulting Letterhead</title>
<link rel="stylesheet" href="https://fonts.googleapis.com/css2?family=Arimo:wght@400;700&family=Questrial&display=swap">
<style>
  :root {
    --backdrop: #e4e4e4;
    --paper: #fcfcfc;
    --brand-teal: #015f6f;
    --brand-mint: #67c296;
    --ink: #555555;
    --signature-tone: #d9d9d9;
  }
  * { margin: 0; padding: 0; box-sizing: border-box; }
  html, body {
    width: 1200px;
    height: 1079px;
    overflow: hidden;
    background: var(--backdrop);
  }
  .letterhead {
    position: absolute;
    left: 267px;
    top: 70px;
    width: 665px;
    height: 940px;
    background: var(--paper);
  }
  .header-bands {
    position: absolute;
    left: 0;
    top: 51px;
    width: 380px;
    height: 40px;
  }
  .brand {
    position: absolute;
    left: 356px;
    top: 50px;
    display: flex;
    align-items: center;
    gap: 10px;
  }
  .brand-mark {
    width: 40px;
    height: 40px;
    border-radius: 50%;
    background: var(--brand-teal);
    flex: none;
  }
  .brand-name {
    font-family: "Questrial", sans-serif;
    font-size: 17px;
    line-height: 19px;
    letter-spacing: 1.6px;
    text-transform: uppercase;
    color: var(--brand-teal);
  }
  .salutation {
    position: absolute;
    left: 61px;
    top: 289px;
    font-family: "Questrial", sans-serif;
    font-weight: 400;
    font-size: 15px;
    color: var(--ink);
    -webkit-text-stroke: 0.4px var(--ink);
  }
  .letter-body {
    position: absolute;
    left: 60px;
    top: 332px;
    width: 548px;
    font-family: "Arimo", sans-serif;
    font-size: 10.6px;
    line-height: 13.6px;
    color: var(--ink);
  }
  .letter-body p + p { margin-top: 11.5px; }
  .closing {
    position: absolute;
    left: 61px;
    top: 614px;
    font-family: "Arimo", sans-serif;
    font-weight: 700;
    font-size: 8px;
    color: var(--ink);
  }
  .signature {
    position: absolute;
    left: 60px;
    top: 653px;
    width: 110px;
    height: 34px;
    background: linear-gradient(90deg, var(--signature-tone), #ececec);
  }
</style>
</head>
<body>
  <main class="letterhead">
    <svg class="header-bands" viewBox="0 0 380 40" aria-hidden="true">
      <polygon points="0,0 373,0 357,29 0,29" fill="var(--brand-teal)"/>
      <polygon points="0,29 357,29 365,39 0,39" fill="var(--brand-mint)"/>
    </svg>
    <div class="brand">
      <span class="brand-mark"></span>
      <span class="brand-name">Brightwell Peak<br>Consulting</span>
    </div>

    <h1 class="salutation">Dear Mr. Ellison,</h1>

    <section class="letter-body">
      <p>Lorem ipsum dolor sit amet, consectetuer adipiscing elit, sed diam nonmmy nibh euismod tincidunt ut laor eet dolore magna aliquam erat volutpat. Ut wisi enim ad minim veniam, quis nostrud exerci tationmcorper suscipit lobortis nisl ut aliquip ex ea commodo consequat. Duis autem vel eum iriure dolor in hendrerit in vulputate velit esse molestie consequat, vel illum dolore eu feugiat</p>
      <p>Rorem ipsum dolor sit amet, consectetuer adipiscing elit, sed diam nonmmy nibh euismod tincidunt ut laor eet dolore magna aliquam erat volutpat. Ut wisi enim ad minim veniam, quis nostrud exerci tationmcorper suscipit lobortis nisl ut aliquip ex ea commodo consequat. Duis autem vel eum iriure dolor in hendrerit in vulputate velit esse molest</p>
      <p>Dorem ipsum dolor sit amet, consectetuer adipiscing elit, sed diam nonmmy nibh euismod tincidunt ut laor eet dolore magna aliquam erat volutpat. Ut wisi enim ad minim veniam, quis nostrud exerci tationmcorper suscipit lobortis nisl ut aliquip ex ea commodo consequat. Duis autem vel eum iriure dolor in hendrerit in suscipit lobortis nisl ut aliquip ex ea commodo consequat. Duis autem vel eum iriure dolor in hendrerit in vulputate velit esse molestie consequat, vel illum</p>
      <p>Sorem ipsum dolor sit amet, consectetuer adipiscing elit, sed diam nonmmy nibh euismod tincidunt ut laor eet dolore magna aliquam erat volutpat. Ut wisi enim ad minim veniam, quis nostrud exerci tationmcorper suscipit lobortis nisl ut aliquip ex ea commodo consequat. Duis autem vel eum iriure dolor in</p>
    </section>

    <p class="closing">Sincerely,</p>
    <div class="signature" role="img" aria-label="Handwritten signature of the sender"></div>
  </main>
</body>
</html>
```